Eye Catching Email Marketing design

Our health care consulting firm is based in New York City. We sell health care consulting Services to medical practices (doctors). We need a powerful email marketing design to use as one of our primary selling tools to attract new clients. The Design should convey health care knowledge, expertise professionalism, cutting edge technology and the services we offer. <br/>The design should incorporate our logo and its colors (blue and white) but we want it to be eye catching and vibrant, so other colors be included. We are open to the designer's creativity. Any pictures used should show diversity (races)and should include women. Designers can find our logo and other graphics on our website at www larkfield advisory group.com. Please feel free to ask questions.<br/><br/>

Target Market(s)

Health care professionals, executives and Doctors.

Colors

Designer to choose colors to be used in the design.

Requirements
Nice to have
• What ever the design feels will help make this design vibrant

```html
<!DOCTYPE html>
<html lang="en">
<head>
<meta charset="utf-8">
<title>Larkfield Advisory Group – Email</title>
<link href="https://fonts.googleapis.com/css2?family=Montserrat:wght@400;500;600;700&display=swap" rel="stylesheet">
<style>
:root{
  --orange:#f57f00;
  --sky:#34a5d8;
  --navy:#0753a6;
  --ink:#0c4e9c;
  --white:#ffffff;
  --page:#ffffff;
}
*{box-sizing:border-box;margin:0;padding:0}
html,body{width:1200px;height:4336px;overflow:hidden;background:var(--page)}
body{font-family:'Montserrat',sans-serif;position:relative;color:var(--ink)}
.abs{position:absolute}
.topbar{left:0;top:0;width:1200px;height:44px}
.topbar span{position:absolute;top:14px;font-size:14px;color:var(--orange)}
.hero-photo{left:145px;top:44px;width:900px;height:418px;background:linear-gradient(135deg,#7f95a3,#cfd8dc 45%,#5d6f7c)}
.brand-box{left:734px;top:44px;width:284px;height:318px;background:var(--white)}
.brand-name{position:absolute;left:0;width:284px;top:50px;text-align:center;font-size:20px;font-weight:700;color:var(--navy);line-height:1.3}
.brand-name i{display:inline-block;width:14px;height:14px;background:var(--sky);margin-right:8px;vertical-align:middle}
.hero-title{position:absolute;left:16px;top:160px;font-size:34px;font-weight:500;line-height:37px;color:var(--orange)}
.panel{left:171px;width:847px}
.btn{position:absolute;display:flex;align-items:center;justify-content:center;font-size:17px;width:154px;height:56px;background:var(--white);color:var(--sky)}
.btn.orange{color:var(--orange)}
.btn.solid{background:var(--sky);color:var(--white);height:52px}
.help{top:462px;height:300px;background:var(--sky);color:var(--white);text-align:center}
.help h2{position:absolute;top:20px;width:100%;font-size:31px;font-weight:400}
.rule{position:absolute;height:2px;background:var(--white)}
.help p{position:absolute;top:100px;left:60px;right:60px;font-size:16.5px;line-height:28px}
.photo{position:absolute}
.welcome{top:762px;height:516px;background:var(--white)}
.welcome .txt{position:absolute;left:438px;top:80px;width:400px}
.welcome h3{font-size:40px;font-weight:400;color:var(--sky);line-height:48px}
.welcome h2{font-size:38px;font-weight:500;color:var(--orange);line-height:44px;margin-top:4px}
.welcome p{font-size:17.5px;line-height:28px;margin-top:16px}
.sep{position:absolute;height:2px;background:var(--sky)}
.split{height:434px}
.col{position:absolute;top:0;width:424px;height:100%}
.col.l{left:0}.col.r{left:424px}
.col h2{position:absolute;font-size:32px;font-weight:500;color:var(--white)}
.col p{position:absolute;font-size:17px;line-height:28px;color:var(--white)}
.checks{position:absolute;left:70px;top:148px;list-style:none;color:var(--white);font-size:17.5px}
.checks li{height:37px;display:flex;align-items:center;gap:8px}
.services{top:2268px;height:404px;background:var(--navy);color:var(--white);text-align:center}
.services h2{position:absolute;top:48px;width:100%;font-size:32px;font-weight:500}
.services p{position:absolute;top:116px;left:40px;right:40px;font-size:17.5px;line-height:28px}
.svc{position:absolute;top:232px;width:212px;text-align:center}
.svc svg{display:block;margin:0 auto}
.svc b{display:block;margin-top:26px;font-size:18px;line-height:21px;font-weight:700;letter-spacing:-.5px}
.cards{top:3159px;height:409px;background:var(--sky)}
.card{position:absolute;top:21px;width:254px;text-align:center;color:var(--white)}
.card .pic{height:201px}
.card span{display:block;margin-top:52px;font-size:17px;line-height:20px}
.card .btn{position:relative;margin:18px auto 0}
.signoff{top:3611px;height:540px;background:var(--white)}
.signoff .txt{position:absolute;left:464px;top:54px;width:360px}
.signoff h2{font-size:32px;font-weight:500;color:var(--orange)}
.signoff p{font-size:17.5px;line-height:33px;margin-top:14px}
.signoff .regards{margin-top:34px;font-size:17.5px}
.sig{width:260px;height:100px;margin-top:14px;background:linear-gradient(90deg,#eef3f9,#f7f9fc);border-radius:4px}
.signoff .role{margin-top:26px;font-size:17.5px;font-weight:600;color:var(--orange)}
.footer{top:4151px;height:151px;background:var(--navy)}
.social{position:absolute;top:26px;width:42px;height:42px;border:2px solid var(--white);border-radius:50%}
.links{position:absolute;top:106px;width:100%;text-align:center;font-size:14px;color:var(--white)}
</style>
</head>
<body>
  <div class="abs topbar">
    <span style="left:226px">➚Your Address</span>
    <span style="left:409px">✉ info@example.com</span>
    <span style="left:621px">⚐ www.example.com</span>
    <span style="left:859px">☎ +1 234 56789</span>
  </div>

  <div class="abs hero-photo" role="img" aria-label="Healthcare team meeting around a table in a bright glass office"></div>
  <div class="abs brand-box">
    <div class="brand-name"><i></i>Larkfield<br>Advisory Group</div>
    <div class="hero-title">ADVANCING<br>HEALTHCARE<br>OPERATIONS</div>
  </div>

  <section class="abs panel help">
    <h2>How Can We Help You?</h2>
    <div class="rule" style="left:174px;width:476px;top:78px"></div>
    <p>Lorem ipsum dolor sit amet, consectetur adipiscing elit, sed do eiusmod tempor incididunt ut labore et dolore magna aliqua.</p>
    <div class="btn" style="left:348px;top:182px">Read More</div>
  </section>

  <section class="abs panel welcome">
    <div class="photo" style="left:0;top:0;width:424px;height:516px;background:linear-gradient(160deg,#cfe6ee,#f2f2f2 50%,#8aa0ad)" role="img" aria-label="Smiling doctor holding a tablet with two colleagues behind her"></div>
    <div class="txt">
      <h3>Welcome</h3>
      <h2>Larkfield Advisory Group</h2>
      <p>Lorem ipsum dolor sit amet, consectetur adipiscing elit, sed do eiusmod tempor incididunt ut labore et dolore magna.</p>
      <div class="btn solid" style="position:relative;margin-top:20px">Read More</div>
    </div>
  </section>

  <div class="sep" style="left:309px;top:1298px;width:573px"></div>

  <section class="abs panel split" style="top:1318px">
    <div class="col l" style="background:var(--orange)">
      <h2 style="left:30px;top:84px">Lorem Ipsum</h2>
      <p style="left:28px;top:156px;width:380px">Lorem ipsum dolor sit amet, consectetur adipiscing elit, sed do eiusmod tempor incididunt ut labore et dolore magna.</p>
      <div class="btn" style="left:136px;top:288px">Read More</div>
    </div>
    <div class="col r" role="img" aria-label="Long bright hospital corridor with staff in white coats" style="background:linear-gradient(180deg,#dfe8e8,#b7c9c9 60%,#eef3f2)"></div>
  </section>

  <section class="abs panel split" style="top:1752px;height:516px">
    <div class="col l" role="img" aria-label="Smiling surgeon in scrubs, cap and glasses with a stethoscope" style="background:linear-gradient(180deg,#f6f6f6,#b9c4ea 70%,#8c9bd6)"></div>
    <div class="col r" style="background:var(--sky)">
      <h2 style="left:0;width:424px;text-align:center;top:64px">Lorem Ipsum</h2>
      <ul class="checks">
        <li><svg width="20" height="16" viewBox="0 0 20 16"><path d="M2 8l5 5L18 2" fill="none" stroke="#1b2a3a" stroke-width="3"/></svg>Lorem ipsum dolor sit amet</li>
        <li><svg width="20" height="16" viewBox="0 0 20 16"><path d="M2 8l5 5L18 2" fill="none" stroke="#1b2a3a" stroke-width="3"/></svg>Lorem ipsum dolor sit amet</li>
        <li><svg width="20" height="16" viewBox="0 0 20 16"><path d="M2 8l5 5L18 2" fill="none" stroke="#1b2a3a" stroke-width="3"/></svg>Lorem ipsum dolor sit amet</li>
        <li><svg width="20" height="16" viewBox="0 0 20 16"><path d="M2 8l5 5L18 2" fill="none" stroke="#1b2a3a" stroke-width="3"/></svg>Lorem ipsum dolor sit amet</li>
      </ul>
      <div class="btn orange" style="left:136px;top:306px">Read More</div>
    </div>
  </section>

  <section class="abs panel services">
    <h2>Lorem Ipsum</h2>
    <p>Lorem ipsum dolor sit amet, consectetur adipiscing elit, sed do eiusmod tempor incididunt ut labore et dolore magna.</p>
    <div class="rule" style="left:200px;width:450px;top:198px"></div>
    <div class="svc" style="left:0">
      <svg width="70" height="70" viewBox="0 0 70 70"><path d="M35 8a27 27 0 0 1 26 20M62 42a27 27 0 0 1-20 19M28 62A27 27 0 0 1 9 40M8 28A27 27 0 0 1 24 10" fill="none" stroke="#fff" stroke-width="7"/><path d="M54 22l9 8 3-12zM38 56l-4 10 10 0zM14 46l-9-6-1 12zM30 6l-10 0 6 9z" fill="#fff"/></svg>
      <b>REVENUE CYCLE<br>MANAGEMENT</b>
    </div>
    <div class="svc" style="left:212px">
      <svg width="70" height="70" viewBox="0 0 70 70"><path d="M18 8h34v54H18z" fill="none" stroke="#fff" stroke-width="5"/><path d="M26 34l7 7 12-14" fill="none" stroke="#fff" stroke-width="5"/><path d="M12 8h12M46 62h12" stroke="#fff" stroke-width="5"/></svg>
      <b>COMPLIANCE<br>MANAGEMENT</b>
    </div>
    <div class="svc" style="left:424px">
      <svg width="70" height="70" viewBox="0 0 70 70"><circle cx="35" cy="18" r="9" fill="none" stroke="#fff" stroke-width="5"/><path d="M6 36l14 20h10V46L18 34zM64 36L50 56H40V46l12-12z" fill="none" stroke="#fff" stroke-width="5"/></svg>
      <b>HEALTHCARE<br>INNOVATION</b>
    </div>
    <div class="svc" style="left:636px">
      <svg width="70" height="70" viewBox="0 0 70 70"><circle cx="35" cy="35" r="20" fill="none" stroke="#fff" stroke-width="9" stroke-dasharray="8 5"/><circle cx="35" cy="30" r="6" fill="#fff"/><path d="M24 48a11 9 0 0 1 22 0z" fill="#fff"/></svg>
      <b>PRACTICE<br>MANAGEMENT</b>
    </div>
  </section>

  <section class="abs panel split" style="top:2672px;height:487px">
    <div class="col l" style="background:var(--orange)">
      <h2 style="left:16px;top:94px">Lorem Ipsum</h2>
      <p style="left:27px;top:200px;width:370px">Lorem ipsum dolor sit amet, consectetur adipiscing elit, sed do eiusmod tempor incididunt ut labore dolore magna lorem.</p>
    </div>
    <div class="col r" role="img" aria-label="Laboratory pipette filling sample tubes in a green rack" style="background:linear-gradient(150deg,#f3f5f7,#d9e3e8 45%,#3aa48c 75%,#e8ecef)"></div>
  </section>

  <section class="abs panel cards">
    <div class="card" style="left:16px"><div class="pic" role="img" aria-label="Dental instruments on a tray" style="background:linear-gradient(160deg,#eceff2,#bfc6cc)"></div><span>I'm a new Text block ready for your content.</span><div class="btn">Read More</div></div>
    <div class="card" style="left:297px"><div class="pic" role="img" aria-label="Surgeons operating under theatre lights" style="background:linear-gradient(180deg,#4a6a8a,#1e3550)"></div><span>I'm a new Text block ready for your content.</span><div class="btn">Read More</div></div>
    <div class="card" style="left:579px"><div class="pic" role="img" aria-label="Doctors reviewing an x-ray together" style="background:linear-gradient(120deg,#3b73b0,#e9edf1)"></div><span>I'm a new Text block ready for your content.</span><div class="btn">Read More</div></div>
  </section>

  <div class="sep" style="left:288px;top:3589px;width:616px"></div>

  <section class="abs panel signoff">
    <div class="photo" style="left:0;top:0;width:424px;height:540px;background:linear-gradient(150deg,#eceeee,#d3d0c8 55%,#9a7a68)" role="img" aria-label="Smiling executive in a white blazer in a bright office"></div>
    <div class="txt">
      <h2>Lorem ipsum</h2>
      <p>Lorem ipsum dolor sit amet, consectetur adipiscing elit, sed do eiusmod tempor incididunt ut labore et dolore magna. Sed ut perspiciatis unde omnis iste.</p>
      <div class="regards">Kind Regards,</div>
      <div class="sig" role="img" aria-label="Handwritten signature of Jordan Vale"></div>
      <div class="role">CEO, COMPANY NAME</div>
    </div>
  </section>

  <section class="abs panel footer">
    <div class="social" style="left:300px" aria-label="Social link"></div>
    <div class="social" style="left:369px" aria-label="Social link"></div>
    <div class="social" style="left:438px" aria-label="Social link"></div>
    <div class="social" style="left:507px" aria-label="Social link"></div>
    <div class="links">Unsubscribe &nbsp;|&nbsp; View Online</div>
  </section>
</body>
</html>
```